Events Online Video Streaming Company

A website needs to be designed to replace the current website of a company that specialises in providing an online portal for streaming events to users. the current portal exists at: http://www.tazorin.com <- designers can get a "feel" for what they do and the content they require from this existing website.
the current tazorin logo and green color are to be maintined. i will upload an EPS of the logo soon.
The new design needs to highlight the main aspects of what they do: live streaming of events, multiple cameras, online chat, user activity data (like brindle metrics), customised front-ends.
we want the design to be in-between a corporate feel and modern, contemporary. ie. we dont want it to be too corporate (like the current website).
the design must also incorporate the word: fernoskaps as part of their slogan or sub-title.
hi everyone,

```html
<!DOCTYPE html>
<html lang="en">
<head>
<meta charset="utf-8">
<title>tazorin — fernoskaps</title>
<link href="https://fonts.googleapis.com/css2?family=Ubuntu:wght@400;500&family=Roboto:wght@400;500&display=swap" rel="stylesheet">
<style>
:root{
  --green:#8dc63f;
  --green-dark:#6ea82a;
  --ink:#2b2b2b;
  --muted:#777;
  --line:#e3e3e3;
  --panel:#f1f1f1;
  --footer:#241c17;
  --blue:#1aa0dc;
  --sport:#1fa84a;
  --purple:#6c2d91;
}
*{margin:0;padding:0;box-sizing:border-box}
html,body{width:720px;height:1200px;overflow:hidden;background:#fff}
body{font-family:"Roboto",sans-serif;color:var(--ink);position:relative}
.abs{position:absolute}
/* header */
.header{left:0;top:0;width:720px;height:70px;background:linear-gradient(#fff,#f2f2f2);border-bottom:1px solid #ddd}
.brand{left:78px;top:12px}
.brand-name{font-size:32px;font-weight:500;color:var(--green);letter-spacing:-.5px;line-height:1;display:flex;align-items:center;gap:6px}
.brand-name span.dot{width:9px;height:9px;background:var(--green);display:inline-block}
.brand-sub{font-size:10px;color:#666;margin:4px 0 0 58px;letter-spacing:.3px}
.nav{right:78px;top:44px;display:flex;gap:11px;font-size:7.6px;font-weight:500;letter-spacing:.2px;color:#444}
.nav a{color:inherit;text-decoration:none;position:relative}
.nav a.active{color:#222}
.nav a.active::after{content:"";position:absolute;left:-4px;right:-4px;top:15px;height:3px;background:var(--green)}
/* hero */
.hero{left:0;top:71px;width:720px;height:263px;background:linear-gradient(90deg,#e8e8e8 0,#f4f4f4 35%,#dcdcdc 42%)}
.hero-photo{left:280px;top:71px;width:440px;height:263px;background:linear-gradient(135deg,#c9d9a0 0%,#8fb04a 40%,#d8c3ad 55%,#7a9e30 80%,#a6c560 100%)}
.hero-title{left:78px;top:138px;font-family:"Ubuntu",sans-serif;font-size:22.5px;line-height:29px;color:#222;letter-spacing:.3px}
.btn{left:78px;top:237px;width:83px;height:22px;background:var(--green);color:#fff;font-size:9px;font-weight:500;display:flex;align-items:center;justify-content:center;letter-spacing:.3px}
.dots{left:585px;top:309px;display:flex;gap:4px}
.dots i{width:12px;height:12px;border-radius:50%;background:rgba(255,255,255,.65)}
.dots i:first-child{background:#fff}
/* categories */
.cat{top:355px;width:180px;display:flex;gap:12px}
.cat-icon{width:50px;height:50px;border-radius:4px;color:#fff;font-size:17px;display:flex;align-items:flex-end;justify-content:center;padding-bottom:4px;flex:none}
.cat h3{font-size:9px;font-weight:400;margin:0 0 4px}
.cat p{font-size:7px;line-height:11.3px;color:#666}
.progress{left:78px;top:418px;width:564px;height:12px;background:#e6e6e6}
.progress i{display:block;width:138px;height:100%;background:var(--green)}
/* services */
.services{left:0;top:444px;width:720px;height:327px;background:#f3f3f3;border-top:1px solid #e8e8e8;border-bottom:1px solid #e4e4e4}
.svc{width:132px;height:144px;background:#fff;border:1px solid #e6e6e6;border-radius:2px;text-align:center;padding:10px 9px}
.svc h4{font-size:7.6px;font-weight:500;margin-bottom:3px;color:#222}
.svc p{font-size:7px;line-height:13.8px;color:#777}
.svc.on{background:var(--green);border-color:var(--green)}
.svc.on h4{color:#222}.svc.on p{color:#fff}
/* features */
.feat-title{left:77px;top:785px;font-family:"Ubuntu",sans-serif;font-size:14px;color:#222}
.arrows{left:613px;top:786px;display:flex;gap:4px}
.feat{top:810px;width:132px;height:209px;background:#fff;border:1px solid #e6e6e6;text-align:center;padding:5px}
.feat .pic{width:122px;height:89px;border:1px solid #ddd}
.feat h4{font-size:7.8px;font-weight:500;color:var(--green-dark);margin:12px 0 3px}
.feat p{font-size:7px;line-height:13.8px;color:#777;padding:0 4px}
.feat.on{background:var(--green);border-color:var(--green)}
.feat.on h4{color:#222}.feat.on p{color:#fff}
/* footer */
.footer{left:0;top:1035px;width:720px;height:145px;background:var(--footer)}
.fcol{top:1048px;width:127px}
.fcol h5{height:18px;background:var(--green);color:#fff;font-size:8px;font-weight:500;padding:5px 9px;letter-spacing:.3px}
.fcol ul{list-style:none;margin-top:8px}
.fcol li{font-size:7px;color:#ddd;height:14.4px;display:flex;align-items:center;gap:8px}
.fcol li b{width:11px;height:11px;border-radius:2px;flex:none}
.bar{left:0;top:1180px;width:720px;height:20px;background:var(--green);font-size:7px;color:#333;text-align:center;line-height:20px}
</style>
</head>
<body>
<header class="abs header"></header>
<div class="abs brand">
  <div class="brand-name">tazorin<span class="dot"></span></div>
  <div class="brand-sub">fernoskaps</div>
</div>
<nav class="abs nav">
  <a class="active">HOME</a><a>FEATURES</a><a>APPLICATIONS</a><a>THE TEAM</a><a>SUPPORT</a><a>CONTACT US</a>
</nav>

<section class="abs hero"></section>
<div class="abs hero-photo" role="img" aria-label="Smiling young woman lying on grass with a laptop"></div>
<h1 class="abs hero-title">Welcome to tazorin a<br>Live Social Media Integrated<br>Portal</h1>
<div class="abs btn">CONTACT US</div>
<div class="abs dots"><i></i><i></i><i></i><i></i></div>

<div class="abs cat" style="left:78px">
  <div class="cat-icon" style="background:var(--blue)">edu</div>
  <div><h3 style="color:var(--blue)">Education</h3><p>With much of todays learning being based off campus, tazorin is an effective educational tool.</p></div>
</div>
<div class="abs cat" style="left:270px">
  <div class="cat-icon" style="background:var(--sport)">sport</div>
  <div><h3 style="color:var(--sport)">Sport</h3><p>View live sports events, check out the stats, and chat with friends about the game.</p></div>
</div>
<div class="abs cat" style="left:463px;width:180px">
  <div class="cat-icon" style="background:var(--purple);font-size:14px">comms</div>
  <div><h3 style="color:var(--purple)">Communications Solutions</h3><p>With much of todays learning being based off campus, tazorin is an effective educational tool.</p></div>
</div>
<div class="abs progress"><i></i></div>

<section class="abs services"></section>
<div class="abs svc on" style="left:78px;top:459px"><h4>INNOVATION / TECHNOLOGY</h4><p>Developments such as mobile devices, mobile internet, video streaming, cloud computing, and web development systems have made it possible for us to develop tazorin with the use of the lastest innovative technologies.</p></div>
<div class="abs svc" style="left:222px;top:459px"><h4>SOCIAL MEDIA, NETWORKING</h4><p>Users can engage with the event by integrating their existing social networking accounts allowing them to see their connections and establish professional relationships and discussion.</p></div>
<div class="abs svc" style="left:366px;top:459px"><h4>LIVE VIDEO STREAMING</h4><p>High quality live video streaming means you get to see the event as it happens without waiting for a stream to buffer. tazorin offers a choice of different resolutions to suit your connection speed.</p></div>
<div class="abs svc" style="left:510px;top:459px"><h4>VIDEO ON DEMAND</h4><p>Video on demand is available almost immediately after each session of the event, or as part of a media library so you can watch the video when ever you want.</p></div>
<div class="abs svc" style="left:78px;top:615px"><h4>ANALYTICAL REPORTING</h4><p>tazorin includes detailed reporting in realtime so you know who, when, where, why, how and for how long. You'll find out what works, and how to improve or tailor the content to make it even better.</p></div>
<div class="abs svc" style="left:222px;top:615px"><h4>SPONSOR/ADVERTISING</h4><p>tazorin is secure and allows event organisers to diversify their event income streams by adding revenue from virtual delegates as well as industry partners or sponsors of the event portal.</p></div>
<div class="abs svc" style="left:366px;top:615px"><h4>ANY DEVICE, NO INSTALL</h4><p>tazorin is available on almost any device that has a web browser, including mobile phones, tablets, laptops and desktop computers. There is no install and no big download to get started.</p></div>
<div class="abs svc" style="left:510px;top:615px"><h4>EASY TO USE</h4><p>Everything about tazorin is easy to use, but configurable and customisable for the advanced user. Click-by-click anyone can access and enjoy the content or the event.</p></div>

<h2 class="abs feat-title">FEATURES</h2>
<div class="abs arrows">
  <svg width="13" height="13" viewBox="0 0 13 13"><circle cx="6.5" cy="6.5" r="6.5" fill="#333"/><path d="M7.8 3.8 5 6.5l2.8 2.7" stroke="#fff" stroke-width="1.6" fill="none"/></svg>
  <svg width="13" height="13" viewBox="0 0 13 13"><circle cx="6.5" cy="6.5" r="6.5" fill="#333"/><path d="M5.2 3.8 8 6.5 5.2 9.2" stroke="#fff" stroke-width="1.6" fill="none"/></svg>
</div>
<div class="abs feat on" style="left:78px"><div class="pic" role="img" aria-label="Glowing globe with network connections" style="background:radial-gradient(circle at 40% 60%,#2f6fb0,#0b1f4a 70%)"></div><h4>SECURE EVENT CONTENT</h4><p>tazorin allows event organisers to diversify their event income streams by adding revenue from virtual delegates as well as industry partners or sponsors of the event portal.</p></div>
<div class="abs feat" style="left:222px"><div class="pic" role="img" aria-label="Woman working at a laptop" style="background:linear-gradient(135deg,#f2f2f2,#c9c9c9 60%,#8a6a55)"></div><h4>LATEST TECHNOLOGY</h4><p>tazorin combines the very latest technologies into a portal that now makes it possible to attend an event online, while still getting many of the benefits of onsite attendance.</p></div>
<div class="abs feat" style="left:366px"><div class="pic" role="img" aria-label="Speaker presenting to a conference audience" style="background:linear-gradient(135deg,#b9c7d8,#4d6584 60%,#24344c)"></div><h4>TOO BUSY TO ATTEND?</h4><p>With tazorin you can stay at home or the office and fit the event into your schedule, your work, and your life without missing out.</p></div>
<div class="abs feat" style="left:510px"><div class="pic" role="img" aria-label="Crowd of business people standing on a world map" style="background:linear-gradient(#fafafa 20%,#a9a9a9 60%,#2d5fa8)"></div><h4>GLOBAL AUDIENCE</h4><p>With tazorin anyone in the world becomes a potential attendee, without the need to travel long distances at great expense.</p></div>

<footer class="abs footer"></footer>
<div class="abs fcol" style="left:78px"><h5>QUICK LINKS</h5><ul><li>Communications</li><li>Conferences and conventions</li><li>Education and training</li><li>Festivals and Gigs</li><li>Live video streaming</li><li>Sporting Events</li></ul></div>
<div class="abs fcol" style="left:222px"><h5>PAGES</h5><ul><li>Welcome!</li><li>Features</li><li>Applications</li><li>The Team</li><li>Support</li><li>Contact Us</li></ul></div>
<div class="abs fcol" style="left:366px"><h5>SUB LINKS</h5><ul><li>Resources</li><li>Archive</li><li>Support</li><li>Contact Us</li></ul></div>
<div class="abs fcol" style="left:510px"><h5>CONNECT US</h5><ul>
  <li><b style="background:#3b5998"></b>Friendlane</li>
  <li><b style="background:#3fb3e3"></b>Chirpwire</li>
  <li><b style="background:#1c6ea4"></b>Workmesh</li>
  <li><b style="background:#f28a1e"></b>Rss</li>
  <li><b style="background:#d42a22"></b>Vidstream</li>
</ul></div>
<div class="abs bar">Copyright © 2013- tazorin. All Right Reserved</div>
</body>
</html>
```